high-impact, conversion-focused website redesign for the government sector

Objective: To design and develop a high-impact, conversion-focused digital platform that solidifies Harrowgate Lumen Advisors (HLA) as the leading communications and strategy firm for government, defense, and industrial clients. The site must project authority, innovation, and sophisticated precision. See the creative breif for more information

Target Market(s)

Government contractors

Industry/Entity Type

Government, defense, industrials

Coding

Coded - Design and coding required

Number of Pages Required

5+ page

Font styles to use
Other font styles liked:
• See the current website

Requirements
Must have
• See design brief
Nice to have
• See design brief
Should not have
• See design brief

```html
<!DOCTYPE html>
<html lang="en">
<head>
<meta charset="utf-8">
<title>Harrowgate Lumen Advisors — Accelerate Your Mission</title>
<link href="https://fonts.googleapis.com/css2?family=Michroma&family=Lexend:wght@300;400;500;600;700&display=swap" rel="stylesheet">
<style>
:root{
  --bg:#0e1014;
  --bg-nav:#0b0d11;
  --navy:#0f2643;
  --navy-deep:#0c1f38;
  --blue:#1e8cf0;
  --green:#8cc63f;
  --orange:#f7941d;
  --white:#ffffff;
  --ink:#1c2430;
  --muted:#5b6573;
  --head:"Michroma",sans-serif;
  --body:"Lexend",sans-serif;
}
*{margin:0;padding:0;box-sizing:border-box}
html,body{width:1200px;height:4089px;overflow:hidden}
body{background:var(--bg);color:var(--white);font-family:var(--body);position:relative}
.abs{position:absolute}
h2.section-title{font-family:var(--head);font-weight:400;font-size:24px;letter-spacing:1px;text-align:center;color:var(--white)}
.btn{display:inline-flex;align-items:center;justify-content:center;height:30px;padding:0 16px;font-size:11px;font-weight:600;text-transform:uppercase;color:var(--white);background:var(--blue);clip-path:polygon(12px 0,calc(100% - 12px) 0,100% 50%,calc(100% - 12px) 100%,12px 100%,0 50%);text-decoration:none;letter-spacing:.3px;white-space:nowrap}
.brand{display:flex;align-items:center;gap:8px;font-family:var(--body);font-weight:500;color:var(--white);text-transform:uppercase;letter-spacing:1px;white-space:nowrap}
.brand-square{width:14px;height:14px;background:var(--blue)}

/* nav */
.nav{top:0;left:0;width:1200px;height:63px;background:var(--bg-nav)}
.nav a{color:var(--white);text-decoration:none;font-size:11px;text-transform:uppercase;position:absolute;top:26px;white-space:nowrap}
.nav .brand{position:absolute;left:530px;top:24px;font-size:11px}

/* hero */
.hero{top:63px;left:0;width:1200px;height:604px;overflow:hidden}
.hero-photo{position:absolute;inset:0;background:linear-gradient(180deg,#2d4660 0%,#4b6f8f 35%,#6a7f92 60%,#3b4858 100%)}
.hero-shade{position:absolute;inset:0;background:rgba(10,20,35,.35)}
.hero h1{position:absolute;top:172px;width:100%;text-align:center;font-family:var(--head);font-weight:400;font-size:46px;letter-spacing:.5px}
.hero p{position:absolute;top:238px;width:100%;text-align:center;font-size:12px;font-weight:500}
.hero .cta{position:absolute;top:293px;left:0;width:100%;display:flex;justify-content:center;gap:18px}
.hero-shapes{position:absolute;left:0;top:0}

/* stats */
.stat{top:576px;width:312px;height:160px;background:var(--white);color:var(--ink);text-align:center}
.stat .num{font-family:var(--head);font-size:38px;margin-top:30px;color:#101820}
.stat p{font-size:10.5px;color:var(--muted);width:220px;margin:14px auto 0;line-height:1.45}
.stat .mark{position:absolute;right:16px;top:14px;width:16px;height:16px;background:var(--blue)}

/* services */
.svc{width:229px;height:152px;background:var(--white);color:var(--ink);overflow:hidden}
.svc .icon{position:absolute;left:24px;top:22px;width:58px;height:50px;background:linear-gradient(135deg,#eaf4dc,#d4e9b8);border-radius:6px}
.svc h3{position:absolute;left:24px;top:105px;font-size:13.5px;font-weight:600;line-height:1.2;color:#1a2a40}
.svc .corner{position:absolute;right:0;bottom:0;width:52px;height:52px;background:var(--blue);clip-path:polygon(100% 0,100% 100%,0 100%)}
.svc .corner svg{position:absolute;right:8px;bottom:8px}

/* who */
.who-img{top:1241px;left:113px;width:487px;height:383px;background:linear-gradient(160deg,#2b3a4a 0%,#3f5a64 45%,#1c3a2a 80%,#0f1a14 100%)}
.who{top:1300px;left:652px;width:420px}
.who h2{font-family:var(--head);font-weight:400;font-size:22px;letter-spacing:1px;margin-bottom:18px}
.who p{font-size:10.5px;line-height:1.7;color:#dfe4ea}
.bullets{display:grid;grid-template-columns:205px 215px;row-gap:12px;margin:18px 0 26px}
.bullets li{list-style:none;font-size:11px;font-weight:600;display:flex;align-items:center;gap:8px;white-space:nowrap}
.bullets li::before{content:"";width:10px;height:10px;border-radius:50%;background:var(--blue)}

/* testimonials */
.testi-band{top:1643px;left:0;width:1200px;height:487px;background:linear-gradient(180deg,var(--navy-deep),var(--navy))}
.testi{top:1811px;width:312px;height:246px;background:var(--white);color:var(--ink);text-align:center}
.testi.active{border:3px solid var(--green)}
.avatar{width:54px;height:54px;border-radius:50%;background:linear-gradient(160deg,#c7ccd3,#8d96a3);margin:24px auto 12px}
.stars{color:#f6b700;font-size:13px;letter-spacing:1px}
.testi p{font-size:10.5px;line-height:1.75;color:var(--muted);width:270px;margin:10px auto 14px}
.testi .name{font-size:11px;font-weight:600;color:#1a2030}
.testi .role{font-size:10px;color:#9aa2ad}
.dots{top:2085px;left:0;width:1200px;display:flex;justify-content:center;gap:5px}
.dots span{width:8px;height:8px;border-radius:50%;background:#c6ccd4}
.dots span.on{background:var(--green)}

/* edge */
.edge{top:2236px;left:113px;width:410px}
.edge h2{font-family:var(--head);font-weight:400;font-size:22px;letter-spacing:1px;margin-bottom:16px}
.edge p{font-size:10.5px;line-height:1.7;color:#dfe4ea;margin-bottom:10px}
.edge-img{top:2193px;left:606px;width:481px;height:292px;background:linear-gradient(180deg,#5f86ad 0%,#9ab7cf 45%,#6b7280 70%,#3d4148 100%)}

/* expect */
.wheel{top:2550px;left:100px;width:440px;height:440px;border-radius:50%;background:conic-gradient(from -5deg,#1e8cf0 0deg 70deg,#f7941d 70deg 175deg,#7ab530 175deg 360deg);opacity:.92}
.wheel-core{top:2700px;left:250px;width:140px;height:140px;border-radius:50%;background:radial-gradient(circle,#ffffff 0 30%,#0e1014 31% 70%,#e8ecf0 71%)}
.expect{top:2585px;left:587px;width:495px}
.expect h2{font-family:var(--head);font-weight:400;font-size:23px;letter-spacing:1px;line-height:1.35;margin-bottom:16px}
.expect p{font-size:10.5px;line-height:1.8;color:#dfe4ea;margin-bottom:10px}
.expect .hl{color:var(--orange)}

/* cta band */
.cta-band{top:3062px;left:113px;width:974px;height:154px;background:linear-gradient(90deg,#173557,#1d3d63)}
.cta-band h2{position:absolute;left:56px;top:46px;font-family:var(--head);font-weight:400;font-size:24px;line-height:1.35;letter-spacing:.5px;white-space:nowrap}
.field{position:absolute;top:41px;width:176px;height:30px;background:var(--white);color:#a9b0ba;font-size:9.5px;padding:10px 20px;clip-path:polygon(12px 0,calc(100% - 12px) 0,100% 50%,calc(100% - 12px) 100%,12px 100%,0 50%)}
.send{position:absolute;left:548px;top:80px;width:366px;height:30px}

/* blog */
.post{top:3331px;width:312px;height:315px;background:var(--white);color:var(--ink)}
.post .thumb{position:absolute;left:14px;top:0;width:284px;height:177px}
.post .date{position:absolute;left:14px;top:197px;font-size:10px;color:var(--muted);display:flex;align-items:center;gap:6px}
.post .mark{position:absolute;right:14px;top:195px;width:16px;height:16px;background:var(--blue)}
.post h3{position:absolute;left:14px;top:222px;font-size:14px;font-weight:600;color:#1a2030}
.post p{position:absolute;left:14px;top:245px;width:270px;font-size:10px;line-height:1.55;color:var(--muted)}
.post a{position:absolute;left:14px;top:283px;font-size:10px;font-weight:600;color:var(--blue);text-decoration:none}

/* footer */
.footer{top:3765px;left:0;width:1200px;height:324px;background:linear-gradient(180deg,#0f2745,#133055)}
.footer .brand{position:absolute;left:113px;top:38px;font-size:13px}
.footer .about{position:absolute;left:113px;top:80px;width:240px;font-size:10px;line-height:1.7;color:#dce3ec}
.badges{position:absolute;left:113px;top:155px;display:flex;gap:4px}
.badges span{width:32px;height:32px;background:#e8ecf1}
.fcol{position:absolute;top:45px}
.fcol h4{font-size:13px;font-weight:700;text-transform:uppercase;margin-bottom:14px}
.fcol li{list-style:none;font-size:10.5px;color:#e6ebf1;margin-bottom:9px;white-space:nowrap}
.contact li{display:flex;gap:10px;line-height:1.6}
.footer .rule{position:absolute;left:113px;top:266px;width:974px;height:1px;background:rgba(255,255,255,.25)}
.footer .copy{position:absolute;top:283px;width:100%;text-align:center;font-size:10px;color:#dce3ec}
</style>
</head>
<body>

<header class="nav abs">
  <a href="#" style="left:232px">Advisory Services</a>
  <a href="#" style="left:410px">About Us</a>
  <div class="brand"><span class="brand-square"></span>Harrowgate Lumen</div>
  <a href="#" style="left:732px">Blog</a>
  <a href="#" style="left:829px">Contact</a>
</header>

<section class="hero abs">
  <div class="hero-photo" role="img" aria-label="Wide industrial hangar interior with steel roof trusses and machinery"></div>
  <div class="hero-shade"></div>
  <h1>ACCELERATE YOUR MISSION</h1>
  <p>We empower federal-focused organizations with the strategy, communications, and connections needed to advance mission-critical outcomes</p>
  <div class="cta">
    <a class="btn" href="#" style="width:122px">Get in touch</a>
    <svg width="186" height="30" viewBox="0 0 186 30" aria-hidden="true"><polygon points="12,1 174,1 185,15 174,29 12,29 1,15" fill="none" stroke="#fff" stroke-width="1.3"/><text x="93" y="19" text-anchor="middle" fill="#fff" font-family="Lexend,sans-serif" font-size="11" font-weight="600">EXPLORE OUR SERVICES</text></svg>
  </div>
  <svg class="hero-shapes" width="1200" height="604" viewBox="0 0 1200 604" aria-hidden="true">
    <polygon points="0,540 1200,360 1200,604 0,604" fill="#0e1014"/>
    <polygon points="0,520 200,540 0,604" fill="#f7941d"/>
    <polygon points="1200,380 1200,604 980,604" fill="#8cc63f"/>
  </svg>
</section>

<div class="stat abs" style="left:113px"><span class="mark"></span><div class="num">72%</div><p>increase in database contacts through CRM implementation and targeted marketing campaigns</p></div>
<div class="stat abs" style="left:444px"><span class="mark"></span><div class="num">100+</div><p>introductions to tech-scouting contracts across the DoD and the aerospace &amp; defense ecosystem</p></div>
<div class="stat abs" style="left:775px"><span class="mark"></span><div class="num">570%</div><p>Positioned a client for transformative growth, fueling increase in stock price and attracting $50M AUD in new investment</p></div>

<h2 class="section-title abs" style="top:796px;left:0;width:1200px">OUR SERVICES</h2>

<div class="svc abs" style="left:113px;top:851px"><div class="icon" role="img" aria-label="Network of people icon"></div><h3>Corporate<br>Communication</h3><div class="corner"><svg width="18" height="10" viewBox="0 0 18 10"><path d="M1 5h15M12 1l4 4-4 4" stroke="#fff" stroke-width="1.3" fill="none"/></svg></div></div>
<div class="svc abs" style="left:360px;top:851px"><div class="icon" role="img" aria-label="Handshake with team icon"></div><h3>Public Relation</h3><div class="corner"><svg width="18" height="10" viewBox="0 0 18 10"><path d="M1 5h15M12 1l4 4-4 4" stroke="#fff" stroke-width="1.3" fill="none"/></svg></div></div>
<div class="svc abs" style="left:609px;top:851px"><div class="icon" role="img" aria-label="Government building icon"></div><h3>Government<br>Affairs</h3><div class="corner"><svg width="18" height="10" viewBox="0 0 18 10"><path d="M1 5h15M12 1l4 4-4 4" stroke="#fff" stroke-width="1.3" fill="none"/></svg></div></div>
<div class="svc abs" style="left:857px;top:851px"><div class="icon" role="img" aria-label="Leader with alert icon"></div><h3>Crisis<br>Communications</h3><div class="corner"><svg width="18" height="10" viewBox="0 0 18 10"><path d="M1 5h15M12 1l4 4-4 4" stroke="#fff" stroke-width="1.3" fill="none"/></svg></div></div>
<div class="svc abs" style="left:113px;top:1022px"><div class="icon" role="img" aria-label="Screen with charts icon"></div><h3>Digital<br>Marketing</h3><div class="corner"><svg width="18" height="10" viewBox="0 0 18 10"><path d="M1 5h15M12 1l4 4-4 4" stroke="#fff" stroke-width="1.3" fill="none"/></svg></div></div>
<div class="svc abs" style="left:360px;top:1022px"><div class="icon" role="img" aria-label="Chess piece over team icon"></div><h3>Strategic<br>Connections</h3><div class="corner"><svg width="18" height="10" viewBox="0 0 18 10"><path d="M1 5h15M12 1l4 4-4 4" stroke="#fff" stroke-width="1.3" fill="none"/></svg></div></div>
<div class="svc abs" style="left:609px;top:1022px"><div class="icon" role="img" aria-label="Handshake with coin icon"></div><h3>Investor<br>Relations</h3><div class="corner"><svg width="18" height="10" viewBox="0 0 18 10"><path d="M1 5h15M12 1l4 4-4 4" stroke="#fff" stroke-width="1.3" fill="none"/></svg></div></div>
<div class="svc abs" style="left:857px;top:1022px"><div class="icon" role="img" aria-label="Calendar with gear icon"></div><h3>Event<br>Management</h3><div class="corner"><svg width="18" height="10" viewBox="0 0 18 10"><path d="M1 5h15M12 1l4 4-4 4" stroke="#fff" stroke-width="1.3" fill="none"/></svg></div></div>

<div class="who-img abs" role="img" aria-label="Airport control tower operations room with monitors overlooking an aircraft on the runway"></div>
<section class="who abs">
  <h2>WHO WE ARE</h2>
  <p>Harrowgate Lumen Advisors is a strategic communications firm built for government, defense, and industrial leaders who operate in complex, mission-critical environments. We translate technical challenges into clear narratives, actionable strategies, and measurable impact. Our team brings decades of experience supporting high-stakes programs where precision, alignment, and execution aren't optional—they're essential.</p>
  <ul class="bullets">
    <li>Federal &amp; defense experts</li><li>High-stakes comms specialists</li>
    <li>Mission-focused strategists</li><li>Trusted advisors to innovators</li>
  </ul>
  <a class="btn" href="#" style="width:118px">Learn more</a>
</section>

<div class="testi-band abs"></div>
<h2 class="section-title abs" style="top:1757px;left:0;width:1200px">TESTIMONIALS</h2>
<div class="testi abs" style="left:113px"><div class="avatar" role="img" aria-label="Client portrait"></div><div class="stars">★★★★★</div><p>HLA understands the mission, the environment, and the stakes. Their strategic insight and ability to communicate with precision helped us strengthen key relationships and advance critical priorities</p><div class="name">Grant P.</div><div class="role">General</div></div>
<div class="testi active abs" style="left:444px"><div class="avatar" role="img" aria-label="Client portrait" style="margin-top:21px"></div><div class="stars">★★★★★</div><p>Working with Harrowgate Lumen made a measurable impact on our event strategy and execution. Their network, organization, and ability to secure high-caliber speakers elevated our entire program</p><div class="name">Nora K.</div><div class="role">General</div></div>
<div class="testi abs" style="left:775px"><div class="avatar" role="img" aria-label="Client portrait"></div><div class="stars">★★★★★</div><p>The HLA team operates with the professionalism and precision you expect from top-tier defense partners. Their ability to navigate both policy and communications challenges set them apart</p><div class="name">Daniel Reeves</div><div class="role">General</div></div>
<div class="dots abs"><span></span><span class="on"></span><span></span><span></span><span></span><span></span><span></span></div>

<section class="edge abs">
  <h2>OUR EDGE</h2>
  <p>We combine deep federal sector insight, technical understanding, and a powerful network across government, industry, investors, and media. Our proven approach drives results — from major contract wins and successful M&amp;A to increased valuation, strategic investment, and political support.</p>
  <p>Our strategies begin with your mission and business goals, ensuring every message, relationship, and action advances growth and impact.</p>
  <a class="btn" href="#" style="width:118px;margin-top:8px">Learn more</a>
</section>
<div class="edge-img abs" role="img" aria-label="Vintage four-engine bomber aircraft parked on an airfield under a cloudy sky"></div>

<div class="wheel abs" role="img" aria-label="Service wheel graphic: messaging and connections, building brands and development, PR, IR, government affairs and marketing, around a central driving-growth hub"></div>
<div class="wheel-core abs" aria-hidden="true"></div>

<section class="expect abs">
  <h2>WHAT TO EXPECT WHEN<br>PARTNERING WITH US</h2>
  <p>With <span class="hl">decades of experience</span>, a results-focused methodology, and cutting-edge marketing and communications tools and technologies, we begin every engagement with a discovery and planning process to ensure we are building a strategy that cuts through the noise to achieve our measurable results. <span class="hl">As specialists in government crisis communications</span>, we additionally examine our client's current strategy for risks ensuring we are building on a stable foundation.</p>
  <p>By truly understanding our client's goals, key milestones, potential areas of risk, ideal customer and investor targets, partner profiles, and other key drivers, <span class="hl">we create messaging and strategy that goes beyond traditional brand awareness</span> to meet mission objectives. As a full service firm, we work across all the areas in the graphic.</p>
  <p>Our <span class="hl">time-tested methodology</span> is based on building and executing a strategy aligned with client mission objectives. With the strategy in place, we execute tactics with precision, efficiency, and the highest quality of customer service.</p>
  <a class="btn" href="#" style="width:122px;margin-top:6px">Get in touch</a>
</section>

<section class="cta-band abs">
  <h2>ADVANCE YOUR MISSION<br>WITH PRECISION</h2>
  <div class="field" style="left:548px">Enter Name</div>
  <div class="field" style="left:738px">Enter Email</div>
  <a class="btn send" href="#">Send</a>
</section>

<h2 class="section-title abs" style="top:3277px;left:0;width:1200px">OUR LATEST NEWS &amp; BLOG</h2>

<article class="post abs" style="left:113px"><div class="thumb" role="img" aria-label="Engineer inspecting a jet engine in a workshop" style="background:linear-gradient(160deg,#2b2f36,#7a5a3a 55%,#1f2226)"></div><div class="date"><svg width="11" height="11" viewBox="0 0 11 11"><rect x=".5" y="1.5" width="10" height="9" fill="none" stroke="#5b6573"/><path d="M.5 4h10" stroke="#5b6573"/></svg>June 15, 2025</div><span class="mark"></span><h3>Insights &amp; Analysis</h3><p>Expert updates on defense, government, and technology—clear, concise, and mission-focused</p><a href="#">Learn More →</a></article>
<article class="post abs" style="left:444px"><div class="thumb" role="img" aria-label="Futuristic hangar with aircraft and operators at screens" style="background:linear-gradient(160deg,#0d3a46,#2a8fa0 55%,#0c1c24)"></div><div class="date"><svg width="11" height="11" viewBox="0 0 11 11"><rect x=".5" y="1.5" width="10" height="9" fill="none" stroke="#5b6573"/><path d="M.5 4h10" stroke="#5b6573"/></svg>June 20, 2025</div><span class="mark"></span><h3>Federal Insights</h3><p>Brief strategic perspectives on the trends shaping today's national security landscape</p><a href="#">Learn More →</a></article>
<article class="post abs" style="left:775px"><div class="thumb" role="img" aria-label="Industrial storage silos under a blue sky" style="background:linear-gradient(180deg,#4f86c6,#a9c3dc 50%,#8a9099)"></div><div class="date"><svg width="11" height="11" viewBox="0 0 11 11"><rect x=".5" y="1.5" width="10" height="9" fill="none" stroke="#5b6573"/><path d="M.5 4h10" stroke="#5b6573"/></svg>June 25, 2025</div><span class="mark"></span><h3>Mission-Focused Updates</h3><p>Short, impactful insights to help leaders navigate the federal ecosystem with confidence</p><a href="#">Learn More →</a></article>

<a class="btn abs" href="#" style="left:548px;top:3675px;width:104px">View all</a>

<footer class="footer abs">
  <div class="brand"><span class="brand-square"></span>Harrowgate Lumen</div>
  <p class="about">Harrowgate Lumen Advisors delivers strategic communications, government affairs, and marketing solutions that help federal-focused organizations accelerate mission success</p>
  <div class="badges"><span></span><span></span><span></span><span></span><span></span><span></span></div>
  <div class="fcol" style="left:395px"><h4>Quick Links</h4><ul><li>Home</li><li>Advisory Services</li><li>About Us</li><li>Latest Blog</li><li>Contact Us</li></ul></div>
  <div class="fcol" style="left:620px"><h4>Our Services</h4><ul><li>Corporate Communication</li><li>Public Relations</li><li>Government Affairs</li><li>Crisis Communications</li><li>Digital Marketing</li><li>Strategic Connections</li><li>Investor Relations</li><li>Event Management</li></ul></div>
  <div class="fcol contact" style="left:882px"><h4>Contact Us</h4><ul>
    <li><svg width="14" height="18" viewBox="0 0 14 18"><path d="M7 1a5.5 5.5 0 0 0-5.5 5.5C1.5 11 7 17 7 17s5.5-6 5.5-10.5A5.5 5.5 0 0 0 7 1z" fill="none" stroke="#8cc63f" stroke-width="1.4"/><circle cx="7" cy="6.5" r="2" fill="none" stroke="#8cc63f" stroke-width="1.4"/></svg><span><b>Summit Works Hub</b><br><b>Harrowgate Lumen Advisors</b><br>418 Meridian Ave<br>Suite 220<br>Crestfield TX, 75010</span></li>
    <li style="margin-top:8px"><svg width="16" height="12" viewBox="0 0 16 12"><rect x=".7" y=".7" width="14.6" height="10.6" fill="none" stroke="#8cc63f" stroke-width="1.3"/><path d="M1 1l7 6 7-6" fill="none" stroke="#8cc63f" stroke-width="1.3"/></svg><span>info@harrowgatelumen.example</span></li>
  </ul></div>
  <div class="rule"></div>
  <p class="copy">©Harrowgate Lumen -2025 All rights reserved.</p>
</footer>

</body>
</html>
```